Interim Manager needs a unique and innovative powerpoint template

I work as interim manager, that means I take over a temporary manager job. My target customers are industry companies with an own production.
You will find informations about me in my website www.quvelo.berlin
I need a fantastic powerpoint template for my presentations in pitches or workshops I do. It should be an innovative and professional style. You will find my logo and colors in the attached files. Looking forward for you inspired designs :-)

```html
<!DOCTYPE html>
<html lang="en">
<head>
<meta charset="utf-8">
<title>Quvelo – Presentation Template Overview</title>
<link href="https://fonts.googleapis.com/css2?family=Open+Sans:wght@400;600;700&display=swap" rel="stylesheet">
<style>
:root{
  --page:#dedede;
  --navy:#1a4e72;
  --deep:#0f3f5e;
  --blue:#2378ad;
  --sky:#3a9fd3;
  --cyan:#3cbbd9;
  --slate:#3b6382;
  --ink:#3a3a3a;
  --muted:#8a8a8a;
  --line:#d7dde2;
  --soft:#eef2f5;
}
*{margin:0;padding:0;box-sizing:border-box}
html,body{width:1200px;height:2565px;overflow:hidden;background:var(--page);font-family:"Open Sans",sans-serif;color:var(--ink)}
.canvas{position:relative;width:1200px;height:2565px}
.slide{position:absolute;width:433px;height:243px;background:#fff;overflow:hidden}
.slide.small{width:363px;height:204px}
.abs{position:absolute}
.corner-tl{position:absolute;left:14px;top:4px;width:46px;height:16px}
.corner-br{position:absolute;right:8px;bottom:3px;width:44px;height:14px}
.brand{position:absolute;right:20px;top:11px;font-weight:700;font-size:12px;letter-spacing:.6px;color:var(--navy)}
.brand.light{color:#fff}
.heading{position:absolute;left:0;width:100%;text-align:center;top:20px;font-size:15px;color:var(--navy)}
.heading.bold{font-weight:700;font-size:16px}
.item-title{font-size:6px;font-weight:700;color:var(--navy)}
.item-text{font-size:4.4px;line-height:1.45;color:var(--muted)}
.photo{position:absolute}
.num{font-size:4px;fill:#fff}
</style>
</head>
<body>
<div class="canvas">

<!-- Row 1 -->
<section class="slide" style="left:124px;top:29px">
  <div class="photo" role="img" aria-label="Black and white city skyline seen from a glass tower" style="inset:0;background:linear-gradient(160deg,#f2f3f4 0%,#cfd3d6 45%,#9aa2a8 100%)"></div>
  <svg class="abs" style="inset:0" width="433" height="243" viewBox="0 0 433 243">
    <polygon points="330,0 380,0 433,55 433,95" fill="#0f5f96"/>
    <polygon points="395,0 433,0 433,38" fill="#2b8fcf"/>
    <polygon points="300,0 320,0 433,120 433,135" fill="#ffffff" opacity=".6"/>
    <polygon points="0,150 0,243 90,243" fill="#0f5f96"/>
    <polygon points="0,190 0,243 40,243" fill="#2b8fcf"/>
    <polygon points="60,180 72,180 140,243 128,243" fill="#ffffff" opacity=".7"/>
    <polygon points="400,228 410,228 424,240 414,240" fill="#2b8fcf"/>
  </svg>
  <div class="abs" style="left:0;width:100%;top:80px;text-align:center;font-weight:700;font-size:26px;letter-spacing:1px;color:var(--navy)">QUVELO</div>
  <div class="abs" style="left:0;width:100%;top:146px;text-align:center;font-size:12px;color:#1c2b36">YOUR AWESOME PRESENTATION TITLE HERE</div>
</section>

<section class="slide" style="left:677px;top:29px">
  <div class="photo" role="img" aria-label="Blue toned photo of a hand sketching a rising chart" style="inset:0;background:linear-gradient(120deg,#2f6f9e 0%,#2a6490 55%,#3a7aa8 100%)"></div>
  <div class="abs" style="left:32px;top:38px;font-weight:700;font-size:15px;color:#fff;letter-spacing:.5px">QUVELO</div>
  <div class="abs" style="left:28px;top:111px;font-size:6px;color:#e6eef5">YOUR TITLE HERE</div>
  <div class="abs" style="left:28px;top:124px;font-size:19px;font-weight:600;color:#fff">PRESENTATION TITLE</div>
  <svg class="corner-br" viewBox="0 0 44 14"><polygon points="14,0 22,0 36,14 28,14" fill="#fff"/><polygon points="26,0 30,0 44,14 40,14" fill="#9fd4ee"/><text x="4" y="11" font-size="4" fill="#fff">2</text></svg>
</section>

<!-- Row 2 -->
<section class="slide" style="left:124px;top:287px">
  <div class="photo" role="img" aria-label="Industrial plant with rusty pipes and steel structures under a blue sky" style="inset:0;background:linear-gradient(135deg,#8ea9c2 0%,#6d7b6a 45%,#8b5a3c 70%,#c8d6e2 100%)"></div>
  <svg class="abs" style="inset:0" width="433" height="243" viewBox="0 0 433 243">
    <defs><linearGradient id="panel3" x1="0" y1="0" x2="1" y2="1"><stop offset="0" stop-color="#2f8ccc"/><stop offset="1" stop-color="#1e5f93"/></linearGradient></defs>
    <polygon points="0,0 120,0 260,243 0,243" fill="url(#panel3)"/>
    <polygon points="60,0 80,0 0,60 0,45" fill="#ffffff" opacity=".9"/>
    <polygon points="340,243 380,220 433,220 433,243" fill="#fff"/>
  </svg>
  <div class="abs" style="left:12px;top:16px;font-weight:700;font-size:11px;color:var(--navy)">QUVELO</div>
  <div class="abs" style="left:30px;top:91px;font-size:6px;color:#e6eef5">YOUR TITLE HERE</div>
  <div class="abs" style="left:30px;top:104px;font-size:19px;font-weight:600;color:#fff">PRESENTATION TITLE</div>
  <svg class="corner-br" viewBox="0 0 44 14"><polygon points="14,0 22,0 36,14 28,14" fill="var(--blue)"/><polygon points="26,0 30,0 44,14 40,14" fill="var(--cyan)"/><text x="4" y="11" font-size="4" fill="#fff">3</text></svg>
</section>

<section class="slide" style="left:677px;top:287px">
  <div class="abs" style="left:0;top:0;width:433px;height:100px;background:linear-gradient(90deg,#2e93d1,#1f5f93)"></div>
  <div class="abs" style="left:12px;top:16px;font-weight:700;font-size:11px;color:#fff">QUVELO</div>
  <div class="abs" style="left:0;width:100%;top:20px;text-align:center;font-size:12px;color:#fff">Welcome Message!</div>
  <div class="abs" style="left:0;width:100%;top:38px;text-align:center;font-size:4px;color:#dbe9f4">/ This is the place for subtitle /</div>
  <svg class="abs" style="left:20px;top:80px" width="14" height="14" viewBox="0 0 14 14"><circle cx="7" cy="7" r="6.5" fill="#ffffff" opacity=".45"/></svg>
  <svg class="abs" style="left:400px;top:80px" width="14" height="14" viewBox="0 0 14 14"><circle cx="7" cy="7" r="6.5" fill="#ffffff" opacity=".45"/></svg>
  <div class="photo" role="img" aria-label="Portrait photo of the interim manager" style="left:179px;top:60px;width:76px;height:76px;border-radius:50%;border:3px solid #fff;background:linear-gradient(180deg,#c9d3dc,#6f8599)"></div>
  <div class="abs" style="left:0;width:100%;top:147px;text-align:center;font-size:6.5px;font-weight:700;color:var(--navy)">Lukas Brenner</div>
  <div class="abs" style="left:0;width:100%;top:156px;text-align:center;font-size:4.5px;color:var(--blue)">Interim Manager</div>
  <div class="abs" style="left:78px;width:277px;top:176px;text-align:center;font-size:5px;line-height:1.6;color:#333">Lorem ipsum dolor sit amet, consectetuer adipiscing elit, sed diam nonummy euismod nibh tincidunt ut laoreet dolore magna aliquam volutpat. minim veniam, quis nostrud exerci tation ullamcorper suscipit lobortis nisl ut aliquip ex ea commodo consequat.</div>
  <svg class="corner-br" viewBox="0 0 44 14"><polygon points="14,0 22,0 36,14 28,14" fill="var(--blue)"/><polygon points="26,0 30,0 44,14 40,14" fill="var(--cyan)"/><text x="4" y="11" font-size="4" fill="var(--blue)">4</text></svg>
</section>

<!-- Row 3 -->
<section class="slide" style="left:124px;top:546px">
  <svg class="corner-tl" viewBox="0 0 46 16"><polygon points="0,0 16,0 40,16 24,16" fill="var(--blue)"/><polygon points="20,0 26,0 46,13 40,13" fill="var(--cyan)"/></svg>
  <div class="brand">QUVELO</div>
  <div class="photo" role="img" aria-label="Portrait photo of the interim manager" style="left:65px;top:62px;width:76px;height:76px;border-radius:50%;background:linear-gradient(180deg,#d6dde3,#72889b)"></div>
  <div class="abs" style="left:40px;width:126px;top:145px;text-align:center;font-size:5.5px;font-weight:700;color:var(--navy)">Lukas Brenner</div>
  <div class="abs" style="left:40px;width:126px;top:155px;text-align:center;font-size:4px;color:#555">Interim Manager</div>
  <svg class="abs" style="left:95px;top:164px" width="16" height="7" viewBox="0 0 16 7"><rect x="0" y="0" width="6" height="6" fill="var(--navy)"/><rect x="9" y="0" width="6" height="6" fill="#6bb54a"/></svg>
  <div class="abs" style="left:168px;top:40px;width:1px;height:160px;background:var(--line)"></div>
  <div class="abs" style="left:184px;top:58px;font-size:6.5px;color:#444">WELCOME</div>
  <div class="abs" style="left:184px;top:69px;font-size:13px;color:#222">MESSAGE</div>
  <div class="abs" style="left:184px;top:88px;width:90px;height:1px;background:var(--line)"></div>
  <div class="abs" style="left:184px;top:106px;width:190px;font-size:4.8px;line-height:1.65;color:#444">Sed ut perspiciatis unde omnis iste natus error sit voluptatem accusantium doloremque laudantium, fringilla totama rem aperiam, eaque ipsa quae ab illo inventore veritatis et quasi architecto beatae vitae dicta sunt explicabo. Donec ut volutpat metui. Aliquam tortor lorem, fringilla tempor dignissim at, augue inventore quae ab illo inventore veritatis.</div>
  <div class="abs" style="left:326px;top:184px;font-size:5px;color:#444">Best Regards</div>
  <svg class="abs" style="left:314px;top:194px" width="60" height="14" viewBox="0 0 60 14"><path d="M2 10 C10 2,14 12,20 6 S32 4,36 9 S50 6,58 5" fill="none" stroke="#555" stroke-width=".8"/></svg>
  <svg class="corner-br" viewBox="0 0 44 14"><polygon points="14,0 22,0 36,14 28,14" fill="var(--blue)"/><polygon points="26,0 30,0 44,14 40,14" fill="var(--cyan)"/><text x="4" y="11" font-size="4" fill="var(--blue)">5</text></svg>
</section>

<section class="slide" style="left:677px;top:546px">
  <svg class="corner-tl" viewBox="0 0 46 16"><polygon points="0,0 16,0 40,16 24,16" fill="var(--blue)"/><polygon points="20,0 26,0 46,13 40,13" fill="var(--cyan)"/></svg>
  <div class="brand">QUVELO</div>
  <div class="heading">About Our Company</div>
  <div class="photo" role="img" aria-label="Dark blue toned photo of an industrial production line" style="left:30px;top:77px;width:181px;height:54px;background:linear-gradient(90deg,#1f3b4e,#3a5d72 50%,#1a2f3d)"></div>
  <div class="abs" style="left:33px;top:142px;width:176px;font-size:8.5px;line-height:1.5;color:#555;text-align:justify">Lorem ipsum dolor sit amet, consectetur Suspendisse <b style="color:#222;font-weight:600">placerat</b> gravida magna vel fermentum. Aenean nunc purus</div>
  <div class="abs" style="left:240px;top:78px;font-size:8.5px;color:var(--navy)">Company History</div>
  <div class="abs" style="left:242px;top:99px;width:160px;font-size:4.4px;line-height:1.8;color:var(--muted)">Sed ut perspiciatis unde omnis iste natus error sit ut voluptatem accusantium doloremque laudantium, fringilla adit totama rem aperiam, eaque ipsa quae ab illo inventore veritatis et quasi architecto beatae vitae dicta sunt explicabo. Donec ut volutpat metui. Aliquam tortor lorem, fringilla tempor dignissim at, eaque ipsa quae ab illo inventore veritatis.<br><br>Donec ut volutpat metui. Aliquam tortor lorem, fringilla tempor dignissim at, eaque ipsa quae ab illo inventore veritatis.</div>
  <svg class="corner-br" viewBox="0 0 44 14"><polygon points="14,0 22,0 36,14 28,14" fill="var(--blue)"/><polygon points="26,0 30,0 44,14 40,14" fill="var(--cyan)"/><text x="4" y="11" font-size="4" fill="var(--blue)">6</text></svg>
</section>

<!-- Row 4 -->
<section class="slide" style="left:124px;top:804px">
  <svg class="corner-tl" viewBox="0 0 46 16"><polygon points="0,0 16,0 40,16 24,16" fill="var(--blue)"/><polygon points="20,0 26,0 46,13 40,13" fill="var(--cyan)"/></svg>
  <div class="brand">QUVELO</div>
  <div class="heading">Our Core Values</div>
  <svg class="abs" style="inset:0" width="433" height="243" viewBox="0 0 433 243">
    <g fill="none" stroke="#b9c4cc" stroke-width=".8">
      <path d="M152 84 H190 L210 112"/><path d="M152 138 H183"/><path d="M152 192 H190 L210 165"/>
      <path d="M282 84 H244 L224 112"/><path d="M282 138 H251"/><path d="M282 192 H244 L224 165"/>
    </g>
    <g fill="#8b979f"><circle cx="152" cy="84" r="1.6"/><circle cx="152" cy="138" r="1.6"/><circle cx="152" cy="192" r="1.6"/><circle cx="282" cy="84" r="1.6"/><circle cx="282" cy="138" r="1.6"/><circle cx="282" cy="192" r="1.6"/></g>
    <circle cx="217" cy="138" r="33" fill="#1d5b86"/>
    <text x="217" y="134" text-anchor="middle" font-size="9" fill="#fff" font-family="Open Sans, sans-serif">Core</text>
    <text x="217" y="147" text-anchor="middle" font-size="9" fill="#fff" font-family="Open Sans, sans-serif">Values</text>
  </svg>
  <div class="abs" style="left:40px;top:74px;width:83px;text-align:right"><div class="item-title">Insert title here</div><div class="item-text">Perspiciatis unde omnis iste natus error voluptatem aperiam.</div></div>
  <div class="abs" style="left:40px;top:126px;width:83px;text-align:right"><div class="item-title">Insert title here</div><div class="item-text">Perspiciatis unde omnis iste natus error voluptatem aperiam.</div></div>
  <div class="abs" style="left:40px;top:178px;width:83px;text-align:right"><div class="item-title">Insert title here</div><div class="item-text">Perspiciatis unde omnis iste natus error voluptatem aperiam.</div></div>
  <div class="abs" style="left:310px;top:74px;width:83px"><div class="item-title">Insert title here</div><div class="item-text">Perspiciatis unde omnis iste natus error voluptatem aperiam.</div></div>
  <div class="abs" style="left:310px;top:126px;width:83px"><div class="item-title">Insert title here</div><div class="item-text">Perspiciatis unde omnis iste natus error voluptatem aperiam.</div></div>
  <div class="abs" style="left:310px;top:178px;width:83px"><div class="item-title">Insert title here</div><div class="item-text">Perspiciatis unde omnis iste natus error voluptatem aperiam.</div></div>
  <svg class="corner-br" viewBox="0 0 44 14"><polygon points="14,0 22,0 36,14 28,14" fill="var(--blue)"/><polygon points="26,0 30,0 44,14 40,14" fill="var(--cyan)"/><text x="4" y="11" font-size="4" fill="var(--blue)">7</text></svg>
</section>

<section class="slide" style="left:677px;top:804px">
  <svg class="corner-tl" viewBox="0 0 46 16"><polygon points="0,0 16,0 40,16 24,16" fill="var(--blue)"/><polygon points="20,0 26,0 46,13 40,13" fill="var(--cyan)"/></svg>
  <div class="brand">QUVELO</div>
  <div class="heading">Our Core Values</div>
  <div class="photo" role="img" aria-label="Power pylon against a teal sky" style="left:25px;top:67px;width:128px;height:86px;background:linear-gradient(180deg,#7fb2b8,#3e7c84)"></div>
  <div class="abs" style="left:153px;top:67px;width:128px;height:86px;background:#1b5a84"></div>
  <svg class="abs" style="left:202px;top:78px" width="30" height="26" viewBox="0 0 30 26"><path d="M3 23 V14 M10 23 V10 M17 23 V13 M24 23 V6" stroke="#fff" stroke-width="4"/><path d="M2 12 L10 6 L16 10 L27 2" fill="none" stroke="#fff" stroke-width="2"/><polygon points="23,1 29,0 28,6" fill="#fff"/></svg>
  <div class="abs" style="left:153px;width:128px;top:116px;text-align:center;font-size:5px;color:#fff">Mission Statement</div>
  <div class="abs" style="left:168px;width:98px;top:126px;text-align:center;font-size:3.8px;color:#d3e4ef">There are many variations passages of slightly believable.</div>
  <div class="photo" role="img" aria-label="Engineers in safety vests beside wind turbines and solar panels" style="left:281px;top:67px;width:128px;height:86px;background:linear-gradient(180deg,#9cc3e0,#3f6fa3)"></div>
  <div class="abs" style="left:40px;width:353px;top:172px;text-align:center;font-size:5.2px;line-height:1.6;color:#333">Contrary to popular belief, <b>Lorem Ipsum is not simply random text.</b> It has roots in a piece of classical Latin literature from 45 BC. There are many variations of passages of Lorem Ipsum available, but the majority have suffered alteration in some form, by injected humor, or randomized don't look even slightly believable.</div>
  <svg class="corner-br" viewBox="0 0 44 14"><polygon points="14,0 22,0 36,14 28,14" fill="var(--blue)"/><polygon points="26,0 30,0 44,14 40,14" fill="var(--cyan)"/><text x="4" y="11" font-size="4" fill="var(--blue)">8</text></svg>
</section>

<!-- Row 5 -->
<section class="slide" style="left:124px;top:1063px">
  <svg class="corner-tl" viewBox="0 0 46 16"><polygon points="0,0 16,0 40,16 24,16" fill="var(--blue)"/><polygon points="20,0 26,0 46,13 40,13" fill="var(--cyan)"/></svg>
  <div class="brand">QUVELO</div>
  <div class="heading" style="font-size:12.5px">Services We Provide</div>
  <svg class="abs" style="inset:0" width="433" height="243" viewBox="0 0 433 243" font-family="Open Sans, sans-serif">
    <g fill="#eef2f5"><rect x="30" y="62" width="177" height="38"/><rect x="30" y="116" width="177" height="38"/><rect x="30" y="169" width="177" height="38"/><rect x="225" y="62" width="177" height="38"/><rect x="225" y="116" width="177" height="38"/><rect x="225" y="169" width="177" height="38"/></g>
    <polygon points="168,62 208,62 208,100 155,100" fill="#2fb0d6"/>
    <polygon points="168,116 208,116 208,154 155,154" fill="#2fb0d6"/>
    <polygon points="168,169 208,169 208,207 155,207" fill="#3a9fd3"/>
    <polygon points="363,62 403,62 403,100 350,100" fill="#1f78b4"/>
    <polygon points="363,116 403,116 403,154 350,154" fill="#2d4f97"/>
    <polygon points="363,169 403,169 403,207 350,207" fill="#0f4767"/>
    <g fill="#fff" font-size="10"><text x="188" y="89">01</text><text x="188" y="143">02</text><text x="188" y="196">03</text><text x="383" y="89">04</text><text x="383" y="143">05</text><text x="383" y="196">06</text></g>
    <g fill="#fff" font-size="3"><text x="186" y="95">SERVICE</text><text x="186" y="149">SERVICE</text><text x="186" y="202">SERVICE</text><text x="381" y="95">SERVICE</text><text x="381" y="149">SERVICE</text><text x="381" y="202">SERVICE</text></g>
  </svg>
  <div class="abs" style="left:43px;top:69px;width:115px"><div class="item-title">Insert title here</div><div class="item-text">Sed perspiciatis unde omnis iste natus voluptatem fringilla.</div></div>
  <div class="abs" style="left:43px;top:123px;width:115px"><div class="item-title">Insert title here</div><div class="item-text">Sed perspiciatis unde omnis iste natus voluptatem fringilla.</div></div>
  <div class="abs" style="left:43px;top:176px;width:115px"><div class="item-title">Insert title here</div><div class="item-text">Sed perspiciatis unde omnis iste natus voluptatem fringilla.</div></div>
  <div class="abs" style="left:238px;top:69px;width:115px"><div class="item-title">Insert title here</div><div class="item-text">Sed perspiciatis unde omnis iste natus voluptatem fringilla.</div></div>
  <div class="abs" style="left:238px;top:123px;width:115px"><div class="item-title">Insert title here</div><div class="item-text">Sed perspiciatis unde omnis iste natus voluptatem fringilla.</div></div>
  <div class="abs" style="left:238px;top:176px;width:115px"><div class="item-title">Insert title here</div><div class="item-text">Sed perspiciatis unde omnis iste natus voluptatem fringilla.</div></div>
  <svg class="corner-br" viewBox="0 0 44 14"><polygon points="14,0 22,0 36,14 28,14" fill="var(--blue)"/><polygon points="26,0 30,0 44,14 40,14" fill="var(--cyan)"/><text x="4" y="11" font-size="4" fill="var(--blue)">10</text></svg>
</section>

<section class="slide" style="left:677px;top:1063px">
  <svg class="corner-tl" viewBox="0 0 46 16"><polygon points="0,0 16,0 40,16 24,16" fill="var(--blue)"/><polygon points="20,0 26,0 46,13 40,13" fill="var(--cyan)"/></svg>
  <div class="brand">QUVELO</div>
  <div class="heading" style="font-size:15.5px">Our Business Services</div>
  <div class="photo" role="img" aria-label="Hydro power dam photo" style="left:164px;top:63px;width:50px;height:50px;border-radius:50%;background:linear-gradient(160deg,#8fb6d6,#3c6e8c)"></div>
  <div class="photo" role="img" aria-label="Digital network technology photo" style="left:221px;top:63px;width:50px;height:50px;border-radius:50%;background:linear-gradient(160deg,#6d8aa6,#2b3e57)"></div>
  <div class="photo" role="img" aria-label="Solar panel under a blue sky photo" style="left:135px;top:112px;width:50px;height:50px;border-radius:50%;background:linear-gradient(160deg,#7ec6f0,#1a6fb8)"></div>
  <div class="abs" style="left:192px;top:112px;width:50px;height:50px;border-radius:50%;background:#3aa6d4"></div>
  <svg class="abs" style="left:204px;top:124px" width="26" height="26" viewBox="0 0 26 26"><circle cx="7" cy="7" r="3" fill="#fff"/><circle cx="13" cy="5" r="3" fill="#fff"/><circle cx="19" cy="7" r="3" fill="#fff"/><rect x="4" y="11" width="18" height="6" rx="2" fill="#fff"/><path d="M3 23 L10 17 L15 20 L23 13" fill="none" stroke="#fff" stroke-width="2"/></svg>
  <div class="photo" role="img" aria-label="Warehouse interior photo" style="left:249px;top:112px;width:50px;height:50px;border-radius:50%;background:linear-gradient(160deg,#e3c9a3,#8a6a4d)"></div>
  <div class="photo" role="img" aria-label="Industrial facility at dusk photo" style="left:164px;top:161px;width:50px;height:50px;border-radius:50%;background:linear-gradient(160deg,#a7b8cc,#3d5673)"></div>
  <div class="photo" role="img" aria-label="Wind turbines at sunset photo" style="left:221px;top:161px;width:50px;height:50px;border-radius:50%;background:linear-gradient(160deg,#5f9ab3,#1f4a5f)"></div>
  <div class="abs" style="left:58px;top:74px;width:80px;text-align:center"><div class="item-title">Insert title here</div><div class="item-text">Perspiciatis unde omnis iste natus error voluptatem aperiam.</div></div>
  <div class="abs" style="left:29px;top:124px;width:80px;text-align:center"><div class="item-title">Insert title here</div><div class="item-text">Perspiciatis unde omnis iste natus error voluptatem aperiam.</div></div>
  <div class="abs" style="left:58px;top:174px;width:80px;text-align:center"><div class="item-title">Insert title here</div><div class="item-text">Perspiciatis unde omnis iste natus error voluptatem aperiam.</div></div>
  <div class="abs" style="left:297px;top:74px;width:80px;text-align:center"><div class="item-title">Insert title here</div><div class="item-text">Perspiciatis unde omnis iste natus error voluptatem aperiam.</div></div>
  <div class="abs" style="left:325px;top:124px;width:80px;text-align:center"><div class="item-title">Insert title here</div><div class="item-text">Perspiciatis unde omnis iste natus error voluptatem aperiam.</div></div>
  <div class="abs" style="left:297px;top:174px;width:80px;text-align:center"><div class="item-title">Insert title here</div><div class="item-text">Perspiciatis unde omnis iste natus error voluptatem aperiam.</div></div>
  <svg class="corner-br" viewBox="0 0 44 14"><polygon points="14,0 22,0 36,14 28,14" fill="var(--blue)"/><polygon points="26,0 30,0 44,14 40,14" fill="var(--cyan)"/><text x="4" y="11" font-size="4" fill="var(--blue)">9</text></svg>
</section>

<!-- Row 6 -->
<section class="slide" style="left:124px;top:1322px">
  <svg class="corner-tl" viewBox="0 0 46 16"><polygon points="0,0 16,0 40,16 24,16" fill="var(--blue)"/><polygon points="20,0 26,0 46,13 40,13" fill="var(--cyan)"/></svg>
  <div class="brand">QUVELO</div>
  <div class="heading bold">Services We Provide</div>
  <svg class="abs" style="inset:0" width="433" height="243" viewBox="0 0 433 243" font-family="Open Sans, sans-serif">
    <g fill="none" stroke="#dde3e8" stroke-width="1.2"><circle cx="79" cy="108" r="32"/><circle cx="171" cy="108" r="32"/><circle cx="263" cy="108" r="32"/><circle cx="355" cy="108" r="32"/></g>
    <g fill="none" stroke-width="2.2" stroke-linecap="round">
      <circle cx="79" cy="108" r="32" stroke="#3cbbd9" stroke-dasharray="153 201" transform="rotate(-90 79 108)"/>
      <circle cx="171" cy="108" r="32" stroke="#3a9fd3" stroke-dasharray="129 201" transform="rotate(-90 171 108)"/>
      <circle cx="263" cy="108" r="32" stroke="#2378ad" stroke-dasharray="66 201" transform="rotate(-90 263 108)"/>
      <circle cx="355" cy="108" r="32" stroke="#1a4e72" stroke-dasharray="185 201" transform="rotate(-90 355 108)"/>
    </g>
    <g font-size="12" fill="#333" text-anchor="middle"><text x="79" y="112">76%</text><text x="171" y="112">64%</text><text x="263" y="112">33%</text><text x="355" y="112">92%</text></g>
  </svg>
  <div class="abs" style="left:44px;top:156px;width:70px;text-align:center"><div class="item-title">Add title here</div><div class="item-text">Nullam convalli orci congue aliquet, diam mauri cura urna, mante lectus magna id maximus.</div></div>
  <div class="abs" style="left:136px;top:156px;width:70px;text-align:center"><div class="item-title">Add title here</div><div class="item-text">Nullam convalli orci congue aliquet, diam mauri cura urna, mante lectus magna id maximus.</div></div>
  <div class="abs" style="left:228px;top:156px;width:70px;text-align:center"><div class="item-title">Add title here</div><div class="item-text">Nullam convalli orci congue aliquet, diam mauri cura urna, mante lectus magna id maximus.</div></div>
  <div class="abs" style="left:320px;top:156px;width:70px;text-align:center"><div class="item-title">Add title here</div><div class="item-text">Nullam convalli orci congue aliquet, diam mauri cura urna, mante lectus magna id maximus.</div></div>
  <svg class="corner-br" viewBox="0 0 44 14"><polygon points="14,0 22,0 36,14 28,14" fill="var(--blue)"/><polygon points="26,0 30,0 44,14 40,14" fill="var(--cyan)"/><text x="4" y="11" font-size="4" fill="var(--blue)">11</text></svg>
</section>

<section class="slide" style="left:677px;top:1322px">
  <svg class="corner-tl" viewBox="0 0 46 16"><polygon points="0,0 16,0 40,16 24,16" fill="var(--blue)"/><polygon points="20,0 26,0 46,13 40,13" fill="var(--cyan)"/></svg>
  <div class="brand">QUVELO</div>
  <div class="heading bold">Our Business Path</div>
  <svg class="abs" style="left:144px;top:65px" width="146" height="146" viewBox="0 0 146 146"><circle cx="73" cy="73" r="71" fill="none" stroke="#1d6a96" stroke-width="1.6"/></svg>
  <div class="abs" style="left:172px;top:103px;width:90px;text-align:center;font-size:7.2px;line-height:1.55;color:#333">“Success does not consist in never making mistakes but in never making the same one a second time.”</div>
  <div class="abs" style="left:28px;top:90px;width:90px"><div style="font-size:7px;color:var(--navy)">Insert title here <span style="font-size:16px;color:#7aa8cc;vertical-align:-2px">1</span></div><div class="item-text" style="width:85px">Sed perspiciatis unde omnis iste natus error voluptatum rem aperiam.</div></div>
  <div class="abs" style="left:28px;top:172px;width:90px"><div style="font-size:7px;color:var(--navy)">Insert title here <span style="font-size:16px;color:#7aa8cc;vertical-align:-2px">2</span></div><div class="item-text" style="width:85px">Sed perspiciatis unde omnis iste natus error voluptatum rem aperiam.</div></div>
  <div class="abs" style="left:316px;top:90px;width:92px"><div style="font-size:7px;color:var(--navy)"><span style="font-size:16px;color:#7aa8cc;vertical-align:-2px">3</span> Insert title here</div><div class="item-text" style="text-align:right">Sed perspiciatis unde omnis iste natus error voluptatum rem aperiam.</div></div>
  <div class="abs" style="left:316px;top:172px;width:92px"><div style="font-size:7px;color:var(--navy)"><span style="font-size:16px;color:#7aa8cc;vertical-align:-2px">4</span> Insert title here</div><div class="item-text" style="text-align:right">Sed perspiciatis unde omnis iste natus error voluptatum rem aperiam.</div></div>
  <svg class="corner-br" viewBox="0 0 44 14"><polygon points="14,0 22,0 36,14 28,14" fill="var(--blue)"/><polygon points="26,0 30,0 44,14 40,14" fill="var(--cyan)"/><text x="4" y="11" font-size="4" fill="var(--blue)">12</text></svg>
</section>

<!-- Row 7 -->
<section class="slide" style="left:124px;top:1581px">
  <svg class="corner-tl" viewBox="0 0 46 16"><polygon points="0,0 16,0 40,16 24,16" fill="var(--blue)"/><polygon points="20,0 26,0 46,13 40,13" fill="var(--cyan)"/></svg>
  <div class="brand">QUVELO</div>
  <div class="heading" style="font-size:12.5px">Information Chart</div>
  <svg class="abs" style="inset:0" width="433" height="243" viewBox="0 0 433 243" font-family="Open Sans, sans-serif">
    <circle cx="97" cy="106" r="46" fill="none" stroke="#3cbbd9" stroke-width="7"/>
    <path d="M97 60 A46 46 0 0 1 143 106" fill="none" stroke="#2a97c7" stroke-width="7"/>
    <circle cx="229" cy="114" r="39" fill="none" stroke="#3a82c4" stroke-width="5.5"/>
    <circle cx="345" cy="120" r="33" fill="none" stroke="#0f4767" stroke-width="4"/>
    <text x="97" y="112" text-anchor="middle" font-size="16" fill="#222">3.6</text>
    <text x="97" y="123" text-anchor="middle" font-size="4.5" fill="#333">BILLION+</text>
    <text x="229" y="120" text-anchor="middle" font-size="13" fill="#222">340</text>
    <text x="229" y="130" text-anchor="middle" font-size="4.5" fill="#333">MILLION</text>
    <text x="345" y="126" text-anchor="middle" font-size="11" fill="#222">22</text>
    <text x="345" y="135" text-anchor="middle" font-size="4" fill="#333">MILLION</text>
  </svg>
  <div class="abs" style="left:52px;top:179px;width:90px;text-align:center"><div class="item-title">Available Market</div><div class="item-text">Sed ut perspiciatis unde omnis iste natus voluptatem fringilla.</div></div>
  <div class="abs" style="left:184px;top:179px;width:90px;text-align:center"><div class="item-title">Addressed Market</div><div class="item-text">Sed ut perspiciatis unde omnis iste natus voluptatem fringilla.</div></div>
  <div class="abs" style="left:300px;top:179px;width:90px;text-align:center"><div class="item-title">Untapped Market</div><div class="item-text">Sed ut perspiciatis unde omnis iste natus voluptatem fringilla.</div></div>
  <svg class="corner-br" viewBox="0 0 44 14"><polygon points="14,0 22,0 36,14 28,14" fill="var(--blue)"/><polygon points="26,0 30,0 44,14 40,14" fill="var(--cyan)"/><text x="4" y="11" font-size="4" fill="var(--blue)">13</text></svg>
</section>

<section class="slide" style="left:677px;top:1581px">
  <svg class="corner-tl" viewBox="0 0 46 16"><polygon points="0,0 16,0 40,16 24,16" fill="var(--blue)"/><polygon points="20,0 26,0 46,13 40,13" fill="var(--cyan)"/></svg>
  <div class="brand">QUVELO</div>
  <div class="heading bold">Numeric List Sample</div>
  <svg class="abs" style="left:0;top:70px" width="433" height="20" viewBox="0 0 433 20" font-family="Open Sans, sans-serif">
    <g font-size="20" fill="#2a97c7"><text x="37" y="18">01</text><text x="136" y="18">02</text><text x="235" y="18">03</text><text x="334" y="18">04</text></g>
    <g stroke="#333" stroke-width=".6"><line x1="80" y1="11" x2="120" y2="11"/><line x1="179" y1="11" x2="219" y2="11"/><line x1="278" y1="11" x2="318" y2="11"/></g>
    <g fill="#333"><circle cx="80" cy="11" r="1.2"/><circle cx="120" cy="11" r="1.2"/><circle cx="179" cy="11" r="1.2"/><circle cx="219" cy="11" r="1.2"/><circle cx="278" cy="11" r="1.2"/><circle cx="318" cy="11" r="1.2"/></g>
  </svg>
  <div class="abs" style="left:38px;top:104px;width:66px"><div class="item-title" style="color:var(--blue)">Insert title here</div><div class="item-text" style="margin-top:11px">There are many variation majority have suffered alteration in some form, randomised words which don't look even slightly believable. If you are going to use a passage to anything embarrassing middle of text.</div></div>
  <div class="abs" style="left:137px;top:104px;width:66px"><div class="item-title" style="color:var(--blue)">Insert title here</div><div class="item-text" style="margin-top:11px">There are many variation majority have suffered alteration in some form, randomised words which don't look even slightly believable. If you are going to use a passage to anything embarrassing middle of text.</div></div>
  <div class="abs" style="left:236px;top:104px;width:66px"><div class="item-title" style="color:var(--blue)">Insert title here</div><div class="item-text" style="margin-top:11px">There are many variation majority have suffered alteration in some form, randomised words which don't look even slightly believable. If you are going to use a passage to anything embarrassing middle of text.</div></div>
  <div class="abs" style="left:335px;top:104px;width:66px"><div class="item-title" style="color:var(--blue)">Insert title here</div><div class="item-text" style="margin-top:11px">There are many variation majority have suffered alteration in some form, randomised words which don't look even slightly believable. If you are going to use a passage to anything embarrassing middle of text.</div></div>
  <svg class="corner-br" viewBox="0 0 44 14"><polygon points="14,0 22,0 36,14 28,14" fill="var(--blue)"/><polygon points="26,0 30,0 44,14 40,14" fill="var(--cyan)"/><text x="4" y="11" font-size="4" fill="var(--blue)">14</text></svg>
</section>

<!-- Row 8 -->
<section class="slide" style="left:124px;top:1840px">
  <svg class="corner-tl" viewBox="0 0 46 16"><polygon points="0,0 16,0 40,16 24,16" fill="var(--blue)"/><polygon points="20,0 26,0 46,13 40,13" fill="var(--cyan)"/></svg>
  <div class="brand">QUVELO</div>
  <div class="heading" style="font-size:15.5px">Information Chart</div>
  <svg class="abs" style="inset:0" width="433" height="243" viewBox="0 0 433 243" font-family="Open Sans, sans-serif">
    <g stroke="#e3e7ea" stroke-width=".6"><line x1="62" y1="75" x2="62" y2="190"/><line x1="129" y1="75" x2="129" y2="190"/><line x1="196" y1="75" x2="196" y2="190"/><line x1="263" y1="75" x2="263" y2="190"/><line x1="330" y1="75" x2="330" y2="190"/><line x1="397" y1="75" x2="397" y2="190"/></g>
    <line x1="62" y1="190" x2="397" y2="190" stroke="#c8ced3" stroke-width=".6"/>
    <rect x="62" y="84" width="54" height="9" fill="#3cbbd9"/>
    <rect x="62" y="93" width="67" height="9" fill="#2a97c7"/>
    <rect x="62" y="102" width="194" height="9" fill="#1f78b4"/>
    <rect x="62" y="111" width="80" height="9" fill="#0f4767"/>
    <rect x="62" y="142" width="67" height="9" fill="#3cbbd9"/>
    <rect x="62" y="151" width="54" height="9" fill="#2a97c7"/>
    <rect x="62" y="160" width="261" height="9" fill="#1f78b4"/>
    <rect x="62" y="169" width="80" height="9" fill="#0f4767"/>
    <g font-size="3.5" fill="#fff" text-anchor="end"><text x="113" y="90">40</text><text x="126" y="99">50</text><text x="253" y="108">145</text><text x="139" y="117">60</text><text x="126" y="148">50</text><text x="113" y="157">40</text><text x="320" y="166">195</text><text x="139" y="175">60</text></g>
    <g font-size="4" fill="#888"><text x="32" y="104">Series One</text><text x="32" y="162">Series Two</text></g>
    <g font-size="3.8" fill="#888" text-anchor="middle"><text x="62" y="198">0</text><text x="129" y="198">50</text><text x="196" y="198">100</text><text x="263" y="198">150</text><text x="330" y="198">200</text><text x="397" y="198">250</text></g>
    <g font-size="3.6" fill="#888"><circle cx="155" cy="212" r="1.3" fill="#3cbbd9"/><text x="158" y="213.5">Column 1</text><circle cx="178" cy="212" r="1.3" fill="#2a97c7"/><text x="181" y="213.5">Column 2</text><circle cx="201" cy="212" r="1.3" fill="#1f78b4"/><text x="204" y="213.5">Column 3</text><circle cx="224" cy="212" r="1.3" fill="#0f4767"/><text x="227" y="213.5">Column 4</text></g>
  </svg>
  <svg class="corner-br" viewBox="0 0 44 14"><polygon points="14,0 22,0 36,14 28,14" fill="var(--blue)"/><polygon points="26,0 30,0 44,14 40,14" fill="var(--cyan)"/><text x="4" y="11" font-size="4" fill="var(--blue)">15</text></svg>
</section>

<section class="slide" style="left:677px;top:1840px">
  <svg class="corner-tl" viewBox="0 0 46 16"><polygon points="0,0 16,0 40,16 24,16" fill="var(--blue)"/><polygon points="20,0 26,0 46,13 40,13" fill="var(--cyan)"/></svg>
  <div class="brand">QUVELO</div>
  <div class="heading" style="font-size:15.5px">Information Chart</div>
  <svg class="abs" style="inset:0" width="433" height="243" viewBox="0 0 433 243" font-family="Open Sans, sans-serif">
    <g stroke="#e3e7ea" stroke-width=".6"><line x1="56" y1="75" x2="395" y2="75"/><line x1="56" y1="97" x2="395" y2="97"/><line x1="56" y1="119" x2="395" y2="119"/><line x1="56" y1="141" x2="395" y2="141"/><line x1="56" y1="163" x2="395" y2="163"/></g>
    <line x1="56" y1="185" x2="395" y2="185" stroke="#c8ced3" stroke-width=".6"/>
    <g font-size="3.8" fill="#888" text-anchor="end"><text x="50" y="76">250</text><text x="50" y="98">200</text><text x="50" y="120">150</text><text x="50" y="142">100</text><text x="50" y="164">50</text><text x="50" y="186">0</text></g>
    <g>
      <rect x="61" y="167" width="13" height="18" fill="#3cbbd9"/><rect x="74" y="159" width="13" height="26" fill="#2a97c7"/><rect x="87" y="123" width="13" height="62" fill="#3a82c4"/><rect x="100" y="159" width="13" height="26" fill="#1f78b4"/><rect x="113" y="148" width="13" height="37" fill="#0f4767"/>
      <rect x="146" y="159" width="13" height="26" fill="#3cbbd9"/><rect x="159" y="167" width="13" height="18" fill="#2a97c7"/><rect x="172" y="101" width="13" height="84" fill="#3a82c4"/><rect x="185" y="159" width="13" height="26" fill="#1f78b4"/><rect x="198" y="106" width="13" height="79" fill="#0f4767"/>
      <rect x="231" y="101" width="13" height="84" fill="#3cbbd9"/><rect x="244" y="136" width="13" height="49" fill="#2a97c7"/><rect x="257" y="159" width="13" height="26" fill="#3a82c4"/><rect x="270" y="145" width="13" height="40" fill="#1f78b4"/><rect x="283" y="163" width="13" height="22" fill="#0f4767"/>
      <rect x="316" y="163" width="13" height="22" fill="#3cbbd9"/><rect x="329" y="132" width="13" height="53" fill="#2a97c7"/><rect x="342" y="145" width="13" height="40" fill="#3a82c4"/><rect x="355" y="97" width="13" height="88" fill="#1f78b4"/><rect x="368" y="123" width="13" height="62" fill="#0f4767"/>
    </g>
    <g font-size="3.2" fill="#fff" text-anchor="middle"><text x="67" y="173">40</text><text x="80" y="165">60</text><text x="93" y="129">140</text><text x="106" y="165">60</text><text x="119" y="154">85</text><text x="152" y="165">60</text><text x="165" y="173">40</text><text x="178" y="107">190</text><text x="191" y="165">60</text><text x="204" y="112">180</text><text x="237" y="107">190</text><text x="250" y="142">112</text><text x="263" y="165">60</text><text x="276" y="151">90</text><text x="289" y="169">50</text><text x="322" y="169">50</text><text x="335" y="138">120</text><text x="348" y="151">90</text><text x="361" y="103">200</text><text x="374" y="129">140</text></g>
    <g font-size="3.8" fill="#888" text-anchor="middle"><text x="93" y="193">Series One</text><text x="178" y="193">Series Two</text><text x="263" y="193">Series Three</text><text x="348" y="193">Series Four</text></g>
    <g font-size="3.6" fill="#888"><circle cx="145" cy="212" r="1.3" fill="#3cbbd9"/><text x="148" y="213.5">Column 1</text><circle cx="168" cy="212" r="1.3" fill="#2a97c7"/><text x="171" y="213.5">Column 2</text><circle cx="191" cy="212" r="1.3" fill="#3a82c4"/><text x="194" y="213.5">Column 3</text><circle cx="214" cy="212" r="1.3" fill="#1f78b4"/><text x="217" y="213.5">Column 4</text><circle cx="237" cy="212" r="1.3" fill="#0f4767"/><text x="240" y="213.5">Column 5</text></g>
  </svg>
  <svg class="corner-br" viewBox="0 0 44 14"><polygon points="14,0 22,0 36,14 28,14" fill="var(--blue)"/><polygon points="26,0 30,0 44,14 40,14" fill="var(--cyan)"/><text x="4" y="11" font-size="4" fill="var(--blue)">16</text></svg>
</section>

<!-- Row 9 -->
<section class="slide" style="left:124px;top:2098px">
  <svg class="corner-tl" viewBox="0 0 46 16"><polygon points="0,0 16,0 40,16 24,16" fill="var(--blue)"/><polygon points="20,0 26,0 46,13 40,13" fill="var(--cyan)"/></svg>
  <div class="brand">QUVELO</div>
  <div class="heading" style="font-size:15.5px">Key Points</div>
  <svg class="abs" style="inset:0" width="433" height="243" viewBox="0 0 433 243" font-family="Open Sans, sans-serif">
    <line x1="217" y1="62" x2="217" y2="224" stroke="#d7dde2" stroke-width="2"/>
    <line x1="137" y1="143" x2="297" y2="143" stroke="#d7dde2" stroke-width="2"/>
    <polygon points="217,58 212,64 222,64" fill="#d7dde2"/><polygon points="217,228 212,222 222,222" fill="#d7dde2"/>
    <rect x="148" y="68" width="64" height="70" fill="#3cbbd9"/>
    <rect x="222" y="68" width="64" height="70" fill="#1f78b4"/>
    <rect x="148" y="148" width="64" height="70" fill="#3a9fd3"/>
    <rect x="222" y="148" width="64" height="70" fill="#0f4767"/>
    <g fill="#fff" text-anchor="middle"><text x="180" y="104" font-size="18">1</text><text x="254" y="104" font-size="18">3</text><text x="180" y="184" font-size="18">2</text><text x="254" y="184" font-size="18">4</text>
    <text x="180" y="120" font-size="5">Key Point</text><text x="254" y="120" font-size="5">Key Point</text><text x="180" y="200" font-size="5">Key Point</text><text x="254" y="200" font-size="5">Key Point</text></g>
  </svg>
  <div class="abs" style="left:42px;top:88px;width:80px;text-align:center"><div class="item-title">Insert title here</div><div class="item-text">Perspiciatis unde omnis iste natus voluptatem rem aperiam.</div></div>
  <div class="abs" style="left:42px;top:168px;width:80px;text-align:center"><div class="item-title">Insert title here</div><div class="item-text">Perspiciatis unde omnis iste natus voluptatem rem aperiam.</div></div>
  <div class="abs" style="left:310px;top:88px;width:80px;text-align:center"><div class="item-title">Insert title here</div><div class="item-text">Perspiciatis unde omnis iste natus voluptatem rem aperiam.</div></div>
  <div class="abs" style="left:310px;top:168px;width:80px;text-align:center"><div class="item-title">Insert title here</div><div class="item-text">Perspiciatis unde omnis iste natus voluptatem rem aperiam.</div></div>
  <svg class="corner-br" viewBox="0 0 44 14"><polygon points="14,0 22,0 36,14 28,14" fill="var(--blue)"/><polygon points="26,0 30,0 44,14 40,14" fill="var(--cyan)"/><text x="4" y="11" font-size="4" fill="var(--blue)">17</text></svg>
</section>

<section class="slide" style="left:677px;top:2098px">
  <svg class="corner-tl" viewBox="0 0 46 16"><polygon points="0,0 16,0 40,16 24,16" fill="var(--blue)"/><polygon points="20,0 26,0 46,13 40,13" fill="var(--cyan)"/></svg>
  <div class="brand">QUVELO</div>
  <div class="heading" style="font-size:15.5px">Table Layout Design</div>
  <svg class="abs" style="inset:0" width="433" height="243" viewBox="0 0 433 243" font-family="Open Sans, sans-serif">
    <g id="tableA">
      <rect x="30" y="70" width="180" height="139" fill="#f2f4f6"/>
      <rect x="30" y="70" width="93" height="17" fill="#e6eaee"/>
      <rect x="123" y="70" width="44" height="17" fill="#1f78b4"/><rect x="167" y="70" width="43" height="17" fill="#1f78b4"/>
      <text x="145" y="80" font-size="4" fill="#fff" text-anchor="middle">Info 01</text><text x="188" y="80" font-size="4" fill="#fff" text-anchor="middle">Info 02</text>
      <g stroke="#d7dde2" stroke-width=".5"><line x1="30" y1="105" x2="210" y2="105"/><line x1="30" y1="123" x2="210" y2="123"/><line x1="30" y1="141" x2="210" y2="141"/><line x1="30" y1="159" x2="210" y2="159"/><line x1="30" y1="177" x2="210" y2="177"/><line x1="30" y1="195" x2="210" y2="195"/><line x1="123" y1="87" x2="123" y2="209"/><line x1="167" y1="87" x2="167" y2="209"/></g>
      <g font-size="3.7" fill="#333"><text x="33" y="98">Passages Of Lorem Available.</text><text x="33" y="116">Roots In A Piece Classical Latin.</text><text x="33" y="134">There Are Variations Of Passages.</text><text x="33" y="152">Contrary To Popular Belief.</text><text x="33" y="170">Majority Have Suffered Alteration.</text><text x="33" y="188">Contrary To Popular Belief.</text></g>
      <g font-size="3.7" fill="#333" text-anchor="middle"><text x="145" y="98">Yup</text><text x="188" y="98">Nope</text><text x="145" y="116">Yup</text><text x="188" y="116">Nope</text><text x="145" y="134">Nope</text><text x="188" y="134">Yup</text><text x="145" y="152">Yup</text><text x="188" y="152">Yup</text><text x="145" y="170">Nope</text><text x="188" y="170">Yup</text><text x="145" y="188">Yup</text><text x="188" y="188">Nope</text></g>
    </g>
    <g transform="translate(194 0)">
      <rect x="30" y="70" width="180" height="139" fill="#f2f4f6"/>
      <rect x="30" y="70" width="93" height="17" fill="#e6eaee"/>
      <rect x="123" y="70" width="44" height="17" fill="#1a4e72"/><rect x="167" y="70" width="43" height="17" fill="#1a4e72"/>
      <text x="145" y="80" font-size="4" fill="#fff" text-anchor="middle">Info 01</text><text x="188" y="80" font-size="4" fill="#fff" text-anchor="middle">Info 02</text>
      <g stroke="#d7dde2" stroke-width=".5"><line x1="30" y1="105" x2="210" y2="105"/><line x1="30" y1="123" x2="210" y2="123"/><line x1="30" y1="141" x2="210" y2="141"/><line x1="30" y1="159" x2="210" y2="159"/><line x1="30" y1="177" x2="210" y2="177"/><line x1="30" y1="195" x2="210" y2="195"/><line x1="123" y1="87" x2="123" y2="209"/><line x1="167" y1="87" x2="167" y2="209"/></g>
      <g font-size="3.7" fill="#333"><text x="33" y="98">Passages Of Lorem Available.</text><text x="33" y="116">Roots In A Piece Classical Latin.</text><text x="33" y="134">There Are Variations Of Passages.</text><text x="33" y="152">Contrary To Popular Belief.</text><text x="33" y="170">Majority Have Suffered Alteration.</text><text x="33" y="188">Contrary To Popular Belief.</text></g>
      <g font-size="3.7" fill="#333" text-anchor="middle"><text x="145" y="98">Yup</text><text x="188" y="98">Nope</text><text x="145" y="116">Yup</text><text x="188" y="116">Nope</text><text x="145" y="134">Nope</text><text x="188" y="134">Yup</text><text x="145" y="152">Yup</text><text x="188" y="152">Yup</text><text x="145" y="170">Nope</text><text x="188" y="170">Yup</text><text x="145" y="188">Yup</text><text x="188" y="188">Nope</text></g>
    </g>
  </svg>
  <svg class="corner-br" viewBox="0 0 44 14"><polygon points="14,0 22,0 36,14 28,14" fill="var(--blue)"/><polygon points="26,0 30,0 44,14 40,14" fill="var(--cyan)"/><text x="4" y="11" font-size="4" fill="var(--blue)">18</text></svg>
</section>

<!-- Row 10 -->
<section class="slide small" style="left:46px;top:2358px">
  <svg class="corner-tl" viewBox="0 0 46 16"><polygon points="0,0 16,0 40,16 24,16" fill="var(--blue)"/><polygon points="20,0 26,0 46,13 40,13" fill="var(--cyan)"/></svg>
  <div class="brand" style="font-size:10px;right:16px">QUVELO</div>
  <div class="heading" style="font-size:13px;top:18px">Table Layout Design</div>
  <svg class="abs" style="inset:0" width="363" height="204" viewBox="0 0 363 204" font-family="Open Sans, sans-serif">
    <text x="36" y="70" font-size="4" fill="#333">Special Features:</text>
    <rect x="88" y="60" width="62" height="18" fill="#3a9fd3"/><rect x="150" y="60" width="62" height="18" fill="#2378ad"/><rect x="212" y="60" width="62" height="18" fill="#1f5f93"/><rect x="274" y="60" width="64" height="18" fill="#1a4e72"/>
    <g font-size="4" fill="#fff" text-anchor="middle"><text x="119" y="70.5">Version One</text><text x="181" y="70.5">Version Two</text><text x="243" y="70.5">Version Three</text><text x="306" y="70.5">Version Four</text></g>
    <rect x="25" y="80" width="63" height="96" fill="#9aa3aa"/>
    <rect x="88" y="80" width="250" height="96" fill="#f4f6f8"/>
    <g stroke="#fff" stroke-width=".7"><line x1="25" y1="96" x2="338" y2="96"/><line x1="25" y1="112" x2="338" y2="112"/><line x1="25" y1="128" x2="338" y2="128"/><line x1="25" y1="144" x2="338" y2="144"/><line x1="25" y1="160" x2="338" y2="160"/></g>
    <g stroke="#e0e4e8" stroke-width=".5"><line x1="150" y1="80" x2="150" y2="176"/><line x1="212" y1="80" x2="212" y2="176"/><line x1="274" y1="80" x2="274" y2="176"/></g>
    <g font-size="3.8" fill="#fff" text-anchor="middle"><text x="56" y="90">Feature 1</text><text x="56" y="106">Feature 2</text><text x="56" y="122">Feature 3</text><text x="56" y="138">Feature 4</text><text x="56" y="154">Feature 5</text><text x="56" y="170">Feature 6</text></g>
    <defs><g id="tick"><circle r="3.4" fill="#2a7fb8"/><path d="M-1.6 0 L-0.4 1.3 L1.8 -1.3" fill="none" stroke="#fff" stroke-width=".8"/></g></defs>
    <use href="#tick" x="119" y="88"/><use href="#tick" x="119" y="104"/>
    <use href="#tick" x="181" y="88"/><use href="#tick" x="181" y="104"/><use href="#tick" x="181" y="120"/><use href="#tick" x="181" y="152"/>
    <use href="#tick" x="243" y="88"/><use href="#tick" x="243" y="104"/><use href="#tick" x="243" y="120"/><use href="#tick" x="243" y="136"/><use href="#tick" x="243" y="152"/>
    <use href="#tick" x="306" y="88"/><use href="#tick" x="306" y="104"/><use href="#tick" x="306" y="120"/><use href="#tick" x="306" y="136"/><use href="#tick" x="306" y="152"/><use href="#tick" x="306" y="168"/>
  </svg>
  <svg class="corner-br" viewBox="0 0 44 14"><polygon points="14,0 22,0 36,14 28,14" fill="var(--blue)"/><polygon points="26,0 30,0 44,14 40,14" fill="var(--cyan)"/><text x="4" y="11" font-size="4" fill="var(--blue)">19</text></svg>
</section>

<section class="slide small" style="left:425px;top:2358px;background:#f4f6f8">
  <div class="photo" role="img" aria-label="Dotted world map in light blue" style="left:40px;top:10px;width:290px;height:140px;background:radial-gradient(ellipse at center,#b9d6ea 0%,#d8e7f2 55%,#f4f6f8 100%)"></div>
  <svg class="abs" style="left:127px;top:40px" width="110" height="110" viewBox="0 0 110 110">
    <circle cx="55" cy="55" r="46" fill="#2a97c7"/>
    <polygon points="74,90 92,104 86,82" fill="#2a97c7"/>
    <circle cx="55" cy="55" r="37" fill="#fff"/>
  </svg>
  <div class="abs" style="left:127px;width:110px;top:87px;text-align:center;font-size:10px;line-height:1.35;color:#333">THANK<br>YOU!</div>
  <div class="abs" style="left:20px;top:178px;font-weight:700;font-size:15px;color:var(--navy);letter-spacing:.5px">QUVELO</div>
  <svg class="abs" style="left:100px;top:180px" width="7" height="10" viewBox="0 0 7 10"><path d="M3.5 0 A3.5 3.5 0 0 1 7 3.5 C7 6,3.5 10,3.5 10 C3.5 10,0 6,0 3.5 A3.5 3.5 0 0 1 3.5 0Z" fill="#2a7fb8"/><circle cx="3.5" cy="3.5" r="1.3" fill="#fff"/></svg>
  <div class="abs" style="left:110px;top:180px;font-size:3.6px;line-height:1.5;color:#555">Hafenstraße 12<br>10245 Berlin</div>
  <svg class="abs" style="left:186px;top:180px" width="9" height="9" viewBox="0 0 9 9"><path d="M2 0.5 L3.5 2.8 L2.6 3.8 C3.2 5.2,4 6,5.3 6.5 L6.3 5.5 L8.5 7 L7.5 8.5 C3.5 8,1 5.5,0.5 1.5Z" fill="#2a7fb8"/></svg>
  <div class="abs" style="left:198px;top:182px;font-size:3.6px;color:#555">+49 030 5550 2184</div>
  <svg class="abs" style="left:262px;top:181px" width="10" height="7" viewBox="0 0 10 7"><rect x=".4" y=".4" width="9.2" height="6.2" fill="none" stroke="#2a7fb8" stroke-width=".8"/><path d="M.4 .4 L5 4 L9.6 .4" fill="none" stroke="#2a7fb8" stroke-width=".8"/></svg>
  <div class="abs" style="left:275px;top:179px;font-size:3.6px;line-height:1.5;color:#555">hello@quvelo.berlin<br>www.quvelo.berlin</div>
  <svg class="corner-br" viewBox="0 0 44 14"><polygon points="14,0 22,0 36,14 28,14" fill="var(--blue)"/><polygon points="26,0 30,0 44,14 40,14" fill="var(--cyan)"/><text x="4" y="11" font-size="4" fill="var(--blue)">20</text></svg>
</section>

<section class="slide small" style="left:806px;top:2358px;background:var(--slate)">
  <div class="abs" style="left:58px;top:44px;font-weight:700;font-size:16px;color:#fff;letter-spacing:.5px">QUVELO</div>
  <div class="abs" style="left:50px;top:92px;font-size:18px;font-weight:700;line-height:1.25;color:#fff;text-align:center;width:90px">GET IN<br>TOUCH<br>WITH US</div>
  <svg class="abs" style="left:144px;top:108px" width="7" height="10" viewBox="0 0 7 10"><path d="M3.5 0 A3.5 3.5 0 0 1 7 3.5 C7 6,3.5 10,3.5 10 C3.5 10,0 6,0 3.5 A3.5 3.5 0 0 1 3.5 0Z" fill="#fff"/><circle cx="3.5" cy="3.5" r="1.3" fill="var(--slate)"/></svg>
  <div class="abs" style="left:156px;top:107px;font-size:3.6px;line-height:1.5;color:#e3ebf2">Hafenstraße 12<br>10245 Berlin</div>
  <svg class="abs" style="left:143px;top:128px" width="9" height="9" viewBox="0 0 9 9"><path d="M2 0.5 L3.5 2.8 L2.6 3.8 C3.2 5.2,4 6,5.3 6.5 L6.3 5.5 L8.5 7 L7.5 8.5 C3.5 8,1 5.5,0.5 1.5Z" fill="#fff"/></svg>
  <div class="abs" style="left:156px;top:130px;font-size:3.6px;color:#e3ebf2">+49 030 5550 2184</div>
  <svg class="abs" style="left:142px;top:151px" width="10" height="7" viewBox="0 0 10 7"><rect x=".4" y=".4" width="9.2" height="6.2" fill="none" stroke="#fff" stroke-width=".8"/><path d="M.4 .4 L5 4 L9.6 .4" fill="none" stroke="#fff" stroke-width=".8"/></svg>
  <div class="abs" style="left:156px;top:149px;font-size:3.6px;line-height:1.5;color:#e3ebf2">hello@quvelo.berlin<br>www.quvelo.berlin</div>
</section>

</div>
</body>
</html>
```